Letterhead design of KESTREL POWER THRIFT INC.

we are a energy saving company doing the solar screen, radian barrier, attic insulation, double panel windows. Basically i need the design of the letterhead including my company name, business address, phone numbers, fax number and email address. Main thing i need it look like a huge company and look like very high class. thanks !!

Reason: Please send me more new design about my company! Thanks so much!!

Industry/Entity Type

Business

```html
<!DOCTYPE html>
<html lang="en">
<head>
<meta charset="utf-8">
<title>Kestrel Power Thrift Inc. – Letterhead</title>
<link href="https://fonts.googleapis.com/css2?family=Arimo:wght@400;700&display=swap" rel="stylesheet">
<style>
  :root {
    --paper: #ffffff;
    --ink: #1a1a1a;
    --brand-grey: #58595b;
    --sun-orange: #f7a21b;
    --sun-yellow: #fcd930;
    --rule: #333333;
  }
  * { margin: 0; padding: 0; box-sizing: border-box; }
  html, body { width: 900px; height: 1200px; overflow: hidden; background: var(--paper); }
  .letterhead {
    position: relative;
    width: 900px;
    height: 1200px;
    background: var(--paper);
    font-family: "Arimo", Arial, sans-serif;
    color: var(--ink);
    overflow: hidden;
  }
  .brand {
    position: absolute;
    left: 40px;
    top: 58px;
    display: flex;
    align-items: flex-end;
    gap: 14px;
  }
  .brand-dot {
    width: 78px;
    height: 78px;
    border-radius: 50%;
    background: var(--sun-orange);
  }
  .brand-name {
    font-weight: 700;
    font-size: 20px;
    letter-spacing: -0.2px;
    color: var(--brand-grey);
    margin-bottom: 0;
    line-height: 1;
  }
  .corner-accent {
    position: absolute;
    right: -90px;
    bottom: -110px;
    width: 320px;
    height: 320px;
    border-radius: 50%;
    background: linear-gradient(160deg, var(--sun-orange) 20%, var(--sun-yellow) 90%);
  }
  .footer {
    position: absolute;
    left: 145px;
    top: 1102px;
    display: flex;
    font-size: 15px;
    line-height: 1.3;
  }
  .footer-address { padding-right: 26px; }
  .footer-address strong { font-weight: 700; }
  .footer-divider {
    width: 1px;
    height: 56px;
    background: var(--rule);
    margin-top: 2px;
  }
  .footer-contact { padding-left: 30px; }
</style>
</head>
<body>
  <main class="letterhead">
    <header class="brand">
      <span class="brand-dot"></span>
      <span class="brand-name">KESTREL POWER THRIFT</span>
    </header>

    <div class="corner-accent" aria-hidden="true"></div>

    <footer class="footer">
      <address class="footer-address" style="font-style:normal">
        <strong>Kestrel Power Thrift Inc.</strong><br>
        2280 Marlow Ct Suite<br>
        #310 Houston, TEXAS 77041
      </address>
      <span class="footer-divider"></span>
      <div class="footer-contact">
        Phone 832-555-0148<br>
        Fax&nbsp; 281-555-0192<br>
        Email kestrelpowerthrift@mailbox.com
      </div>
    </footer>
  </main>
</body>
</html>
```